Trade Alert Service needs Vistrel thumbnail / channel design

I'm about to set up a Vistrel channel which gives real-time trade alerts to earn passive income. I'm looking for a Vistrel channel design to include thumbnail and other associated visuals for the channel.
The trade alerts will be focused around selling cash-secured put options on US equities, and directed at people who want investing advice / tips for getting out of the rat race. I'd like the theme to be somewhat serious / credible, without too many eye-popping neon colours like all the other cheap trade alert videos / day trading videos on Vistrel. Happy for you to use your experience if you think otherwise though, as you're the designer, not me!

Target Market(s)

Option Traders, Value Investors, People who want passive income

Industry/Entity Type

Finance

Logo Text

Calm Meadow Wealth Notes

Requirements
Must have
• All relevant Vistrel visuals so that I can upload them to the Vistrel channel - all visuals required by Vistrel Studio upload within the channel creation page.
A logo so that I can append it to Powerpoint presentations
Nice to have
• A blank Powerpoint slide template showing the logo would be great in chosen colour scheme

```html
<!DOCTYPE html>
<html lang="en">
<head>
<meta charset="utf-8">
<title>Trading and Investing – Our Way to Financial Freedom</title>
<link rel="stylesheet" href="https://fonts.googleapis.com/css2?family=Roboto+Slab:wght@400;500;700;800&family=Roboto:wght@400;500&display=swap">
<style>
  :root {
    --stage: #b9b7b8;
    --navy: #0a1421;
    --grid: #1d3a28;
    --gold: #ebbf14;
    --ink: #0a1421;
    --white: #ffffff;
    --arrow-light: #a9dd8b;
    --arrow-mid: #80c563;
    --arrow-deep: #3f8a3a;
    --arrow-edge: #d9e4ea;
    --meadow-light: #7f9b66;
    --meadow-deep: #3f5a2e;
    --sweater: #8a4c24;
    --panel: #f9f9f9;
    --title: #0f0f0f;
    --meta: #606060;
    --cream: #fdebc8;
    --cream-screens: #f4f1ea;
    --teal: #17b4b6;
    --tag: #f2a850;
    --progress: #e21b1b;
  }
  * { margin: 0; padding: 0; box-sizing: border-box; }
  html, body {
    width: 1200px; height: 1200px; overflow: hidden;
    background: var(--stage);
  }
  .canvas { position: relative; width: 1200px; height: 1200px; overflow: hidden; }
  .defs { position: absolute; width: 0; height: 0; }

  /* thumbnail design, built at 922 × 518 */
  .thumbnail {
    position: absolute; width: 922px; height: 518px; overflow: hidden;
    background: var(--navy);
  }
  .thumbnail--feature { left: 140px; top: 53px; }
  .thumbnail-frame {
    position: absolute; left: 19px; top: 648px;
    width: 374px; height: 210px; overflow: hidden;
  }
  .thumbnail--small { left: 0; top: 0; transform: scale(0.4056); transform-origin: 0 0; }
  .thumbnail-art { position: absolute; inset: 0; }

  .topic-band {
    position: absolute; left: 0; top: 37px;
    width: 522px; height: 44px; background: var(--gold);
  }
  .topic-label {
    position: absolute; left: 56px; top: 37px;
    font-family: "Roboto Slab", serif; font-weight: 700;
    font-size: 31px; line-height: 44px; color: var(--ink);
    letter-spacing: -0.6px; white-space: nowrap;
  }
  .dollar-badge {
    position: absolute; left: 508px; top: 31px;
    width: 58px; height: 58px; border-radius: 50%;
    background: var(--gold);
    box-shadow: 0 0 0 3px var(--navy) inset, 0 0 0 6px var(--gold) inset;
    display: flex; align-items: center; justify-content: center;
    font-family: "Roboto Slab", serif; font-weight: 800;
    font-size: 33px; color: var(--ink);
  }
  .headline { position: absolute; left: 54px; top: 88px; font-family: "Roboto Slab", serif; white-space: nowrap; }
  .headline-lead {
    display: block; font-weight: 500; font-size: 43px; line-height: 54px;
    color: var(--gold);
  }
  .headline-key {
    display: block; font-weight: 800; font-size: 67px; line-height: 72px;
    color: var(--gold); letter-spacing: -1px;
  }
  .headline-tail {
    display: block; font-weight: 700; font-size: 38px; line-height: 46px;
    color: var(--white); letter-spacing: 23px;
  }
  .headline-rule {
    position: absolute; left: 56px; top: 264px;
    width: 161px; height: 2px; background: var(--white);
  }

  /* search results listing */
  .results {
    position: absolute; left: 3px; top: 637px; right: 0; bottom: 0;
    background: var(--panel);
  }
  .result-thumb { position: absolute; left: 16px; width: 374px; overflow: hidden; }
  .duration {
    position: absolute; padding: 0 6px; height: 23px;
    background: rgba(15, 10, 10, 0.85); border-radius: 3px;
    font-family: "Roboto", sans-serif; font-weight: 500;
    font-size: 17px; line-height: 23px; color: var(--white);
  }
  .result-title, .result-meta, .result-text {
    position: absolute; left: 414px; white-space: nowrap;
    font-family: "Roboto", sans-serif;
  }
  .result-title { font-size: 27px; line-height: 34px; color: var(--title); }
  .result-meta { font-size: 19px; line-height: 24px; color: var(--meta); }
  .result-text { font-size: 18.5px; line-height: 27px; color: var(--meta); }
  .result-text b { font-weight: 500; color: #404040; }

  .promo-thumb { top: 245px; height: 208px; background: var(--cream); }
  .promo-screens { position: absolute; left: 80px; top: 18px; width: 225px; height: 170px; }
  .promo-label {
    position: absolute; font-family: "Roboto", sans-serif;
    font-size: 14px; line-height: 16px; color: #7a7a7a; letter-spacing: 0.3px;
  }
  .progress-bar { position: absolute; left: 0; bottom: 0; width: 100%; height: 5px; background: var(--progress); }

  .venue-thumb { top: 478px; height: 100px; background: var(--teal); }
  .venue-tag {
    position: absolute; left: 115px; top: 17px; width: 144px; height: 16px;
    background: var(--tag); border: 1px solid #b56a20; border-radius: 2px;
    font-family: "Roboto Slab", serif; font-size: 8px; line-height: 14px;
    color: #6a3510; text-align: center; white-space: nowrap;
  }
</style>
</head>
<body>
<main class="canvas">
  <svg class="defs" width="0" height="0" aria-hidden="true">
    <defs>
      <linearGradient id="meadowTone" x1="0" y1="0" x2="1" y2="0">
        <stop offset="0" style="stop-color:var(--meadow-deep)"/>
        <stop offset="0.45" style="stop-color:var(--meadow-light)"/>
        <stop offset="0.72" style="stop-color:var(--meadow-deep)"/>
        <stop offset="0.82" style="stop-color:var(--sweater)"/>
        <stop offset="0.92" style="stop-color:var(--meadow-light)"/>
        <stop offset="1" style="stop-color:var(--meadow-deep)"/>
      </linearGradient>
      <linearGradient id="arrowTone" x1="0" y1="1" x2="1" y2="0">
        <stop offset="0" style="stop-color:var(--arrow-deep)"/>
        <stop offset="0.45" style="stop-color:var(--arrow-mid)"/>
        <stop offset="1" style="stop-color:var(--arrow-light)"/>
      </linearGradient>
      <pattern id="gridLines" width="31" height="31" patternUnits="userSpaceOnUse">
        <path d="M31 0V31M0 31H31" fill="none" style="stroke:var(--grid)" stroke-width="1"/>
      </pattern>
    </defs>
  </svg>

  <section class="thumbnail thumbnail--feature">
    <svg class="thumbnail-art" width="922" height="518" viewBox="0 0 922 518">
      <rect x="340" y="0" width="582" height="518" fill="url(#meadowTone)"
            role="img" aria-label="Photo of a young woman in a rust sweater with a patterned backpack standing in a green meadow"/>
      <polygon points="0,0 807,0 658,35 705,59 580,229 475,189 323,363 40,518 0,518" style="fill:var(--navy)"/>
      <polygon points="0,0 807,0 658,35 705,59 580,229 475,189 323,363 40,518 0,518" fill="url(#gridLines)"/>
      <polyline points="419,518 531,301 649,357 773,96 816,118" fill="none" style="stroke:var(--arrow-edge)" stroke-width="8"/>
      <polygon points="40,518 323,363 475,189 580,229 705,59 658,35 807,0 816,118 773,96 649,357 531,301 419,518"
               fill="url(#arrowTone)" role="img" aria-label="Rising green arrow filled with a photo of glass office towers"/>
    </svg>
    <div class="topic-band"></div>
    <p class="topic-label">TRADING AND INVESTING</p>
    <div class="dollar-badge">$</div>
    <h1 class="headline">
      <span class="headline-lead">OUR WAY TO</span>
      <span class="headline-key">FINANCIAL</span>
      <span class="headline-tail">FREEDOM</span>
    </h1>
    <div class="headline-rule"></div>
  </section>

  <section class="results">
    <div class="thumbnail-frame" style="left:16px; top:11px;">
      <div class="thumbnail thumbnail--small">
        <svg class="thumbnail-art" width="922" height="518" viewBox="0 0 922 518">
          <rect x="340" y="0" width="582" height="518" fill="url(#meadowTone)"
                role="img" aria-label="Photo of a young woman in a rust sweater with a patterned backpack standing in a green meadow"/>
          <polygon points="0,0 807,0 658,35 705,59 580,229 475,189 323,363 40,518 0,518" style="fill:var(--navy)"/>
          <polygon points="0,0 807,0 658,35 705,59 580,229 475,189 323,363 40,518 0,518" fill="url(#gridLines)"/>
          <polyline points="419,518 531,301 649,357 773,96 816,118" fill="none" style="stroke:var(--arrow-edge)" stroke-width="8"/>
          <polygon points="40,518 323,363 475,189 580,229 705,59 658,35 807,0 816,118 773,96 649,357 531,301 419,518"
                   fill="url(#arrowTone)" role="img" aria-label="Rising green arrow filled with a photo of glass office towers"/>
        </svg>
        <div class="topic-band"></div>
        <p class="topic-label">TRADING AND INVESTING</p>
        <div class="dollar-badge">$</div>
        <div class="headline">
          <span class="headline-lead">OUR WAY TO</span>
          <span class="headline-key">FINANCIAL</span>
          <span class="headline-tail">FREEDOM</span>
        </div>
        <div class="headline-rule"></div>
      </div>
      <span class="duration" style="right:8px; bottom:10px;">1:11</span>
    </div>
    <h2 class="result-title" style="top:10px;">Brightloop: Animated Explainer Video Company</h2>
    <p class="result-meta" style="top:47px;">Brightloop • 6.4K views • 1 year ago</p>
    <p class="result-text" style="top:84px;">We create awesome explainer videos for companies all around the world. Check our our own<br>video to see why we are ...</p>

    <div class="result-thumb promo-thumb">
      <div class="promo-screens" role="img" aria-label="Illustration of website, social and mobile screens showing bicycle ads" style="background:var(--cream-screens); left:82px; width:225px;"></div>
      <span class="promo-label" style="left:35px; top:17px;">VIDEO</span>
      <span class="promo-label" style="left:300px; top:17px;">SOCIAL</span>
      <span class="promo-label" style="left:28px; top:180px;">DISPLAY</span>
      <span class="duration" style="right:7px; bottom:10px;">1:53</span>
      <div class="progress-bar"></div>
    </div>
    <h2 class="result-title" style="top:243px;">Pinverra | Brightloop</h2>
    <p class="result-meta" style="top:279px;">Brightloop • 108 views • 1 year ago</p>
    <p class="result-text" style="top:317px;">Subscribe for more videos, and find out more at: http://www.<b>brightloop</b>.com Or follow us on T<br>https://chirpline.com/<b>brightloop</b> And ...</p>

    <div class="result-thumb venue-thumb" role="img" aria-label="Illustration of a restaurant front with waiters carrying cloches">
      <div class="venue-tag">ACRB Regulations Restaurant</div>
    </div>
    <h2 class="result-title" style="top:476px;">Tallymark | Brightloop</h2>
    <p class="result-meta" style="top:512px;">Brightloop • 53 views • 1 year ago</p>
    <p class="result-text" style="top:550px;">Subscribe for more videos, and find out more at: http://www.<b>brightloop</b>.com Or follow us on T</p>
  </section>
</main>
</body>
</html>
```